Wireless Captive Portal Provider needs a logo and business card design

We need a logo and business card for a new company called Pebblecrest WiFi LLC. The company offers a cloud base service for businesses to provide wireless access to their customers, this is called a captive portal. The captive portal also has the ability to encourage users to check in or tweet at the company which is a major draw so there is a large social media component to the company. We would like to see designs that incorporate the name of the company. We are envisioning a minimalist design, but will entertain any original ideas, especially those that incorporate the social media component.

The company name is Pebblecrest WiFi, so a light a fresh look is desired in the blue and yellow color scheme.

We own www.pebblecrestwifi.example domain name for our site and email as well as @PebblecrestWiFi on twitter. I mention this as this allows us to do the clever business card design that can capture email, twitter, and homepage on a business card. Search google images for "business card twitter email website" for examples.

I would be interested in business card designs that allow for an image of the employee to be added.

Target Market(s)

Our target market are store fronts with customer seating that provide wireless access. Or anywhere we wireless access is provided.

Industry/Entity Type

Business

Contact Information for Business Card

Logo Text

Pebblecrest WiFi, Ltd. Liability Co.

Logo styles of interest
Pictorial/Combination Logo
Abstract Logo
Font styles to use
Sans Serif

Colors
85cae6
fbf289
cadf82
33a6d7
fbee3e
add136
0891cc
fbed22
9bcb3b

Requirements
Nice to have
• We own www.pebblecrestwifi.example domain name for our site and email as well as @PebblecrestWiFi on twitter. I mention this as this allows us to do the clever business card design that can capture email, twitter, and homepage on a business card. Search google images for "business card twitter email website" for examples.

```html
<!DOCTYPE html>
<html lang="en">
<head>
<meta charset="utf-8">
<title>Pebblecrest WiFi — Logo and Business Card</title>
<link rel="stylesheet" href="https://fonts.googleapis.com/css2?family=Questrial&family=Arimo:wght@400;700&display=swap">
<style>
  :root {
    --paper: #ffffff;
    --ink: #231f20;
    --sky: #85cae6;
    --blue: #33a6d7;
    --sun: #fbf289;
    --petal-shade: #f7c9a9;
    --leaf: #cadf82;
    --rule: #333333;
  }
  html, body {
    margin: 0;
    padding: 0;
    overflow: hidden;
    background: var(--paper);
  }
  .canvas {
    position: relative;
    width: 988px;
    height: 1200px;
    overflow: hidden;
    background: var(--paper);
    color: var(--ink);
  }
  .logo-showcase {
    position: absolute;
    left: 0;
    top: 0;
    width: 988px;
    height: 600px;
    display: flex;
    align-items: center;
    justify-content: center;
    gap: 28px;
  }
  .logo-dot {
    width: 96px;
    height: 96px;
    border-radius: 50%;
    background: var(--sky);
  }
  .logo-name {
    font-family: "Questrial", sans-serif;
    font-size: 84px;
    color: var(--ink);
    letter-spacing: 0.5px;
  }
  .business-card {
    position: absolute;
    left: 4px;
    top: 637px;
    width: 978px;
    height: 555px;
    border: 2px solid var(--rule);
    background: var(--paper);
  }
  .card-art {
    position: absolute;
    left: 0;
    top: 0;
    width: 978px;
    height: 555px;
  }
  .card-mark-dot {
    position: absolute;
    left: 98px;
    top: 150px;
    width: 92px;
    height: 92px;
    border-radius: 50%;
    background: var(--sky);
  }
  .card-name {
    position: absolute;
    left: 230px;
    top: 276px;
    margin: 0;
    font-family: "Questrial", sans-serif;
    font-weight: 400;
    font-size: 58px;
    line-height: 1;
    color: var(--ink);
  }
  .photo-slot {
    position: absolute;
    left: 704px;
    top: 18px;
    width: 241px;
    height: 243px;
    border: 2px solid var(--rule);
    display: flex;
    align-items: center;
    justify-content: center;
  }
  .photo-label {
    font-family: "Arimo", sans-serif;
    font-size: 36px;
    color: var(--ink);
    transform: rotate(-32deg);
  }
  .contact {
    position: absolute;
    margin: 0;
    font-family: "Arimo", sans-serif;
    font-size: 19px;
    color: var(--ink);
  }
  .contact-handle { left: 58px; top: 486px; }
  .contact-web { left: 18px; top: 528px; }
  .contact-company { right: 22px; top: 528px; }
</style>
</head>
<body>
  <div class="canvas">
    <section class="logo-showcase" aria-label="Pebblecrest WiFi logo">
      <span class="logo-dot" aria-hidden="true"></span>
      <span class="logo-name">Pebblecrest WiFi</span>
    </section>

    <section class="business-card" aria-label="Business card">
      <svg class="card-art" viewBox="0 0 978 555" aria-hidden="true">
        <path d="M150 250 C 220 268, 110 318, 200 338 C 360 364, 620 352, 790 340"
              fill="none" stroke="var(--leaf)" stroke-width="6" stroke-linecap="round"/>
      </svg>
      <span class="card-mark-dot" aria-hidden="true"></span>
      <h1 class="card-name">Pebblecrest WiFi</h1>
      <div class="photo-slot">
        <span class="photo-label">PHOTO</span>
      </div>
      <p class="contact contact-handle">@PebblecrestWiFi</p>
      <p class="contact contact-web">www.pebblecrestwifi.example</p>
      <p class="contact contact-company">Pebblecrest WiFi LLC.</p>
    </section>
  </div>
</body>
</html>
```